Baked goods front of bag sticker

Pebblecrest Brownies,
2 Go size (clear plastic bag of handful of ¼” square bites)
There will also be larger sizes and custom options(corporate/events) using the same image.
Deliverables Needed:
Need sticker with “Pebblecrest Brownies” for front of bag, approximate 2” circle or rectangle/square.
Packaging front sticker design should be sizable for other media, ie website, future packaging, logo.
Flavor should be indicated on second sticker that integrates well.
Back sticker is already complete and includes ingredients, company name, health dept permit, and other legal necessities. Font will be changed to integrate with front.
Flavors:
1. Sunset Maple Brownie
2. Honeycomb Glow Brownie
3. Zip Zop Mint
4. Crumbly Oat Delight (not so gooey but great)
Primary Audiences:
Anyone who wants a sweet treat to enjoy, and maybe share, on the go. Audience wants a fresh treat with real ingredients they know and love (real butter, Pure vanilla, Fresh eggs)
Audience wants something from a baker not a machine.
Sold at checkout in stores that don’t have baked goods, higher end convenience stores, specialty stores, small gourmet stores, theaters, toy stores, sports arenas, etc.
Will be sampled at events (festivals, movie screenings, races)
Tone and Image:
Fresh, Fun and frank with real ingredients you know
Because it is little and is home-baked, it should be perceived as a little treat without the guilt.
Messages:
Fresh, natural, little treat on the run.
Dear Designers,

```html
<!DOCTYPE html>
<html lang="en">
<head>
<meta charset="utf-8">
<title>Pebblecrest Brownies – Flavour Stickers</title>
<link rel="stylesheet" href="https://fonts.googleapis.com/css2?family=Grand+Hotel&family=Oswald:wght@400&family=Berkshire+Swash&display=swap">
<style>
  :root {
    --ink: #111111;
    --white: #ffffff;
    --paper: #ffffff;
  }
  html, body {
    margin: 0;
    padding: 0;
    width: 1200px;
    height: 1200px;
    overflow: hidden;
    background: var(--paper);
  }
  .sticker-sheet {
    display: block;
    width: 1200px;
    height: 1200px;
  }
  .flavor-honeycomb { --rim: #fdc778; --face: #f9b75b; --ribbon: #fde0b8; }
  .flavor-maple     { --rim: #c48845; --face: #c68a45; --ribbon: #d7ba90; }
  .flavor-mint      { --rim: #7e4d2d; --face: #8b5734; --ribbon: #c6b094; }
  .flavor-oat       { --rim: #84c4bf; --face: #85c4bf; --ribbon: #d6ecea; }

  .badge-rim    { fill: var(--rim); }
  .badge-face   { fill: var(--face); stroke: var(--ink); stroke-width: 3.2; }
  .badge-inner  { fill: none; stroke: var(--ink); stroke-width: 1.4; }
  .stripe       { fill: var(--ink); }
  .star         { fill: var(--ink); }
  .rule         { stroke: var(--ink); stroke-width: 1.3; }
  .ribbon       { fill: var(--ribbon); }

  .brand-name {
    font-family: "Grand Hotel", cursive;
    font-size: 40px;
    fill: var(--white);
    text-anchor: middle;
  }
  .flavor-name {
    font-family: "Berkshire Swash", cursive;
    font-size: 19px;
    fill: var(--ink);
    text-anchor: middle;
  }
  .tagline {
    font-family: "Oswald", sans-serif;
    font-weight: 400;
    font-size: 9.5px;
    letter-spacing: 0.4px;
    fill: var(--white);
    text-anchor: middle;
  }
</style>
</head>
<body>
<svg class="sticker-sheet" viewBox="0 0 1000 1000" xmlns="http://www.w3.org/2000/svg">
  <defs>
    <path id="star-shape" d="M0,-1 L0.235,-0.324 L0.951,-0.309 L0.38,0.124 L0.588,0.809 L0,0.4 L-0.588,0.809 L-0.38,0.124 L-0.951,-0.309 L-0.235,-0.324 Z"/>
    <clipPath id="inner-disc"><circle r="126"/></clipPath>

    <g id="sticker-base">
      <circle class="badge-rim" r="138"/>
      <circle class="badge-face" r="128"/>
      <circle class="badge-inner" r="121"/>

      <g class="stars-top">
        <use class="star" href="#star-shape" transform="translate(-52,-86) scale(7.5)"/>
        <use class="star" href="#star-shape" transform="translate(-28,-94) scale(9)"/>
        <use class="star" href="#star-shape" transform="translate(0,-99) scale(12)"/>
        <use class="star" href="#star-shape" transform="translate(28,-94) scale(9)"/>
        <use class="star" href="#star-shape" transform="translate(52,-86) scale(7.5)"/>
      </g>

      <text class="brand-name" x="0" y="-32">Pebblecrest<tspan x="0" dy="40">Brownies</tspan></text>

      <g class="stripes" clip-path="url(#inner-disc)">
        <rect class="stripe" x="-130" y="-6" width="42" height="2"/>
        <rect class="stripe" x="-130" y="1" width="42" height="4"/>
        <rect class="stripe" x="-130" y="10" width="42" height="2"/>
        <rect class="stripe" x="88" y="-6" width="42" height="2"/>
        <rect class="stripe" x="88" y="1" width="42" height="4"/>
        <rect class="stripe" x="88" y="10" width="42" height="2"/>
      </g>

      <polygon class="ribbon" points="-148,32 148,32 134,50 148,68 -148,68 -134,50"/>

      <text class="tagline" x="0" y="84">BAKED FRESH. SHARED SMALL.</text>

      <line class="rule" x1="-50" y1="100" x2="-12" y2="100"/>
      <use class="star" href="#star-shape" transform="translate(0,101) scale(9)"/>
      <line class="rule" x1="12" y1="100" x2="50" y2="100"/>
    </g>
  </defs>

  <g class="sticker flavor-honeycomb" transform="translate(278,325)">
    <use href="#sticker-base"/>
    <text class="flavor-name" x="0" y="57">Honeycomb Glow</text>
  </g>

  <g class="sticker flavor-maple" transform="translate(723,325)">
    <use href="#sticker-base"/>
    <text class="flavor-name" x="0" y="57">Sunset Maple</text>
  </g>

  <g class="sticker flavor-mint" transform="translate(278,677)">
    <use href="#sticker-base"/>
    <text class="flavor-name" x="0" y="57">Zip Zop Mint</text>
  </g>

  <g class="sticker flavor-oat" transform="translate(723,677)">
    <use href="#sticker-base"/>
    <text class="flavor-name" x="0" y="57">Crumbly Oat Delight</text>
  </g>
</svg>
</body>
</html>
```